Top producing Realtors in Washington, D.C. need cover design for home buying book.

We need a cover design for our printed home buying booklet. Right now our working title is "Capital Area Property's Complete Handbook for Savvy Purchasers". The book guides readers through the homebuying process. The inside of the book is text, real images of homes, rooms, and probably some exterior shots of the Washington, D.C. area. We have a little professor cartoon icon we got from Pictavault.com that we are using inside the book when we have an important point to me made within the text. Think of how guides for beginners have that target with a dart on the bullseye. (We've attached an example of the icon.) We'd like the cover to be graphics that help illustrate the feeling of "smart" "intelligent" but not stuffy, since we do have a slightly cartoonish feel in parts of the inside with the professor icon. So we'd like to include real images of nice parts of a house--living room, kitchen, bathroom, but also a graphic aspect that's not real images. WE'RE OPEN TO OTHER IDEAS! but we just had those thoughts. We want to primarily get across to readers that they are smart--or we can help them be smart--about buying real estate, and this is the guide for them, and we can help them get a nice home.We have an account with pictavault.com and have license to use the attached photos and icon. After seeing some samples, we like the idea of the professor icon on the cover. We might have additional photos, please use pictavault.com and we can download then forward licensed images, so long as their not "editorial only" images. Also, Please include "By Marisa Vendrapolo and Jonathan Wexbrunel somewhere on the cover. Does not have to be prominent but must be there.

The dimensions of the book is is 5.5 inches wide and 8.5 inches long. We would like it to bleed off in all directions.

Target Market(s)

Home buyers

Font styles to use
Serif

Requirements
Must have
• We want to primarily get across to readers that they are smart--or we can help them be smart--about buying real estate, and this is the guide for them. Sophisticated, but not stuffy.

```html
<!DOCTYPE html>
<html lang="en">
<head>
<meta charset="utf-8">
<title>Capital Area Property's Complete Handbook for Savvy Purchasers</title>
<link href="https://fonts.googleapis.com/css2?family=PT+Serif:wght@400;700&display=swap" rel="stylesheet">
<style>
  :root {
    --cover-red: #722227;
    --paper: #ffffff;
    --title-white: #ffffff;
    --byline: #f3ece9;
    --photo-warm: #b89a78;
    --photo-light: #e4e0d8;
    --photo-wood: #7a4a34;
  }
  html, body {
    margin: 0;
    padding: 0;
    overflow: hidden;
    background: var(--cover-red);
  }
  .cover {
    position: relative;
    width: 840px;
    height: 1200px;
    background: var(--cover-red);
    overflow: hidden;
    font-family: "PT Serif", Georgia, serif;
  }
  .photo-strip {
    position: absolute;
    left: 5px;
    top: 0;
    width: 355px;
    height: 1060px;
    background: var(--paper);
  }
  .room-photo {
    position: absolute;
    left: 11px;
    width: 334px;
    height: 198px;
  }
  .room-photo.kitchen-dark { top: 11px; background: linear-gradient(160deg, var(--photo-light) 0%, #c9bfae 55%, var(--photo-wood) 100%); }
  .room-photo.living-room { top: 221px; background: linear-gradient(170deg, #f2f1ed 0%, #dcd8cf 60%, #b9ad98 100%); }
  .room-photo.kitchen-white { top: 430px; background: linear-gradient(165deg, #eef0ea 0%, #d9d6cc 55%, #6e4630 100%); }
  .room-photo.library { top: 640px; background: linear-gradient(160deg, #5b2a24 0%, #7d3a30 45%, #a0765a 100%); }
  .room-photo.bathroom { top: 850px; background: linear-gradient(165deg, #e6e2d8 0%, #d4cbb8 55%, var(--photo-warm) 100%); }

  .cover-title {
    position: absolute;
    right: 30px;
    top: 20px;
    margin: 0;
    text-align: right;
    color: var(--title-white);
    font-weight: 700;
    font-size: 58px;
    line-height: 73px;
    letter-spacing: 0.5px;
  }
  .cover-title span { display: block; }

  .professor-mascot {
    position: absolute;
    left: 400px;
    top: 600px;
    width: 420px;
    height: 536px;
    border-radius: 50% 50% 12px 12px / 40% 40% 12px 12px;
    background: radial-gradient(ellipse at 55% 40%, #f4e6dc 0%, #eadbd0 45%, rgba(234,219,208,0.0) 75%);
  }

  .byline {
    position: absolute;
    left: 0;
    right: 0;
    top: 1128px;
    margin: 0;
    text-align: center;
    padding-left: 8px;
    color: var(--byline);
    font-weight: 400;
    font-size: 28px;
  }
</style>
</head>
<body>
  <main class="cover">
    <section class="photo-strip">
      <div class="room-photo kitchen-dark" role="img" aria-label="Photo of a bright kitchen with white cabinets and a dark wood island"></div>
      <div class="room-photo living-room" role="img" aria-label="Photo of a white living room with sofas and a fireplace"></div>
      <div class="room-photo kitchen-white" role="img" aria-label="Photo of a white kitchen with a marble island and hanging pot rack"></div>
      <div class="room-photo library" role="img" aria-label="Photo of a wood-panelled library with armchairs and arched windows"></div>
      <div class="room-photo bathroom" role="img" aria-label="Photo of a bathroom with a glass shower and a tiled soaking tub"></div>
    </section>

    <h1 class="cover-title">
      <span>CAPITAL</span>
      <span>AREA</span>
      <span>PROPERTY'S</span>
      <span>COMPLETE</span>
      <span>HANDBOOK</span>
      <span>FOR</span>
      <span>SAVVY</span>
      <span>PURCHASERS</span>
    </h1>

    <div class="professor-mascot" role="img" aria-label="Cartoon professor in a white lab coat and round glasses holding a pointer"></div>

    <p class="byline">Marisa Vendrapolo and Jonathan Wexbrunel</p>
  </main>
</body>
</html>
```